Mein Unternehmen heißt 'velunora Pädagogisch-Psychologische Beratung'. velunora ist lateinisch für begleiten. Mein Name ist Torben Walduck, ich bin Pädagoge und Psychologe
Meine Zielgruppe sind
-Eltern (Seminare zu den Bedürfnissen eines Kindes, Bindungs- und Erziehungsberatung)
-pädagogische Fachkräfte (Beratung von Einzelpersonen und Teams in Bindungs und Erziehungsfragen als auch zu Teamprozessen)
-Gerichte (Erstellung familienpsychologischer Gutachten)
My company is called 'velunora educational-psychological consulting'. velunora is Latin for accompany. My name is Torben Walduck, I am an educator and psychologist.
My target groups are
-Parents (seminars on the needs of a child, bonding and educational counseling)
-educational professionals (counseling individuals and teams on attachment and parenting issues as well as team processes)
-courts (preparation of family psychological reports)
Ich hätte gerne einen Flyer (DIN lang, 6 seitig, Maße siehe 'Vorlage Flyer' bei den Dateien), für mein Elternseminar.
Ich möchte einen Flyer, der ein schönes farbliches Konzept hat: professionell aber nicht zu ernst, freundlich-offen aber nicht kitschig.
Das Design soll dann später für Flyer für meine anderen Angebote genutzt werden (als Folgeauftrag/ 1:1 Projekt), dann aber als 4 seitiger Flyer ohne Anmeldeformular.
Text und Inhalte für den Flyer sind im PDF 'Flyer_Inhalte_und_Text'. Alles in ROT sind Hinweise und sollen nicht Teil des Flyers sein.
Ich bin aber offen für Vorschläge z.B. für eine andere Aufteilung der Inhalte.
Ich bin mir nicht sicher, ob ich Stock-Fotos auf dem Flyer haben möchte, aber ich habe mal Beispiele mit hochgeladen, die ich mir vorstellen könnte ('baby' und 'parents'). Es steht den Designern aber auch frei, eigene Stock-Fotos einzufügen, die ich dann erwerben würde.
Von den Farben sollte es sich an dem Grün (R:54 G:197 B:144 (#36C590)) und dem Orange (R:255 G:161 B:2 (#FFA102)) aus dem Logo orientieren.
Die Schriftarten vom Logo sind 'Aller Bold' (Name) und Engravers Gothic BT (Untertitel).
I would like to have a flyer (DIN long, 6 pages, dimensions see 'Template Flyer' at the files), for my parent seminar.
I would like a flyer that has a nice color concept: professional but not too serious, friendly-open but not kitschy.
The design is to be used later for flyers for my other offers (as a follow-up order/ 1:1 project), but then as a 4-page flyer without a registration form.
Text and content for the flyer are in the PDF 'Flyer_Content_and_Text'. Everything in RED are hints and should not be part of the flyer.
However, I am open to suggestions e.g. for a different division of the content.
I'm not sure I want stock photos on the flyer, but I've uploaded examples I could imagine ('baby' and 'parents'). However, designers are also free to add the..

```html
<!DOCTYPE html>
<html lang="de">
<head>
<meta charset="utf-8">
<title>FEST+VERTRAUT – Elternseminar</title>
<link rel="stylesheet" href="https://fonts.googleapis.com/css2?family=Fira+Sans:ital,wght@0,400;1,400&family=Raleway:wght@500&display=swap">
<style>
  :root {
    --orange: #ffa102;
    --green: #4fb88c;
    --green-light: #bfe6d5;
    --panel-grey: #f2f2f2;
    --text: #1f1f1f;
    --photo-a: #6f8f3c;
    --photo-b: #8a6a4a;
  }
  html, body { margin: 0; padding: 0; overflow: hidden; }
  body { width: 1200px; height: 818px; background: #fff; }
  .canvas {
    position: relative; width: 1200px; height: 818px; overflow: hidden;
    font-family: "Fira Sans", sans-serif; color: var(--text);
  }
  .backdrop { position: absolute; inset: 0; }
  .pill {
    position: absolute; height: 33px; background: var(--orange); color: #fff;
    border-radius: 0 17px 17px 0; font-family: "Raleway", sans-serif; font-weight: 500;
    font-size: 12.4px; letter-spacing: 0.4px; line-height: 33px; text-transform: uppercase;
    box-sizing: border-box; padding-left: 20px; white-space: nowrap;
  }
  .block { position: absolute; margin: 0; font-size: 12.4px; line-height: 16.2px; white-space: nowrap; }
  .block p { margin: 0; }
  .accent { color: var(--green); font-style: italic; }
  .bullets { list-style: none; margin: 0; padding: 0; }
  .bullets li { padding-left: 9px; text-indent: -9px; margin-bottom: 4px; }
  .small { font-size: 10.3px; line-height: 14.8px; }
  .subhead {
    position: absolute; margin: 0; font-family: "Raleway", sans-serif; font-weight: 500;
    color: var(--orange); font-size: 12.6px; letter-spacing: 0.3px; text-transform: uppercase;
  }
  .dates p { margin: 0 0 4px; }
</style>
</head>
<body>
<div class="canvas">
  <svg class="backdrop" width="1200" height="818" viewBox="0 0 1200 818" aria-hidden="true">
    <path d="M806,0 L1200,0 L1200,818 L905,818 C945,660 948,490 885,365 C835,265 802,205 806,115 Z" fill="var(--panel-grey)"/>
    <path d="M806,115 C802,205 835,265 885,365 C948,490 945,660 905,818" fill="none" stroke="var(--green-light)" stroke-width="15"/>
    <circle cx="817" cy="10" r="109" fill="var(--green)"/>
    <circle cx="66" cy="790" r="92" fill="var(--green)"/>
  </svg>
  <svg class="backdrop" width="1200" height="818" viewBox="0 0 1200 818" role="img" aria-label="Foto: Elternhände halten ein Paar kleine Babyschuhe vor grüner Wiese">
    <defs>
      <linearGradient id="photoTone" x1="0" y1="0" x2="1" y2="1">
        <stop offset="0" stop-color="var(--photo-b)"/>
        <stop offset="0.45" stop-color="var(--photo-a)"/>
        <stop offset="1" stop-color="#4f7a2a"/>
      </linearGradient>
    </defs>
    <path d="M124,655 C150,655 190,690 230,708 C270,722 318,728 311,762 C305,790 290,805 268,818 L139,818 C105,790 88,745 92,712 C96,685 108,660 124,655 Z" fill="url(#photoTone)"/>
  </svg>

  <div class="pill" style="left:0;top:23px;width:209px;">Warum fest+vertraut?</div>
  <div class="block" style="left:22px;top:66px;">
    <p>Weil ein Kind Nähe und Sicherheit benötigt, damit es sich gut<br>entwickeln kann. Nur dann bekommt das Kind eine gute<br>Grundlage für die Herausforderungen seines Menschenlebens.</p>
  </div>
  <div class="block" style="left:22px;top:131px;">
    <p>Wenn Eltern ein Kind erwarten, wird alles für eine gute Geburt<br>und dessen Gesundheit getan. Darum steht in der Schwanger-<br>schaft einiges an, z. B. Vorsorgeuntersuchungen, Geburtsvorbe-<br>reitungskurs, Wahl einer Hebamme und eines Krankenhauses.</p>
  </div>
  <div class="block" style="left:22px;top:212px;">
    <p>Daneben dann noch die Vorbereitung auf die ersten Lebens-<br>monate des Säuglings. Sollte ich mein Kind stillen und wenn ja,<br>wie lange? Was benötige ich an Kleidung für das Neugeborene?<br>Eventuell soll auch noch ein Kinderzimmer renoviert und mit<br>Möbeln ausgestattet werden. Das ist auch alles richtig und wichtig.<br>Oft wird aber an die Vorbereitung auf einen anderen, wichtigen<br>Punkt nicht gedacht: <span class="accent">Wie sich durch die Geburt eines Kindes auch<br>der Alltag der Eltern verändert.</span></p>
  </div>
  <ul class="block bullets" style="left:22px;top:357px;">
    <li>- Wie lebt man als Familie, so dass die Bedürfnisse<br>des Kindes erfüllt werden, die Bedürfnisse der<br>Eltern aber nicht vernachlässigt werden?</li>
    <li>- Müssen die Rollen innerhalb der Partnerschaft eventuell<br>neu verteilt werden? Wie wird die Versorgung des Kindes<br>und die Berufstätigkeit miteinander vereinbart?</li>
    <li>- Wie erkenne ich z. B., was das Kind braucht, wenn<br>es ausgeschlafen, satt und frisch gewickelt ist,<br>aber trotzdem weint oder schreit?</li>
    <li>- Wie entwickelt sich ein Kind gut, wie wächst es FEST+VERTRAUT auf?</li>
  </ul>
  <div class="block" style="left:22px;top:547px;">
    <p>Das Seminar soll Ihnen dabei helfen, dass Sie ihrer Familie schon<br>vorher eine gute Struktur geben können. Es werden die wichtigsten<br>Themen der Säuglings– und Kleinkindzeit besprochen. Es wird<br>Raum für die Fragen der Eltern geben und die Möglichkeit, sich mit<br>den eigenen Erfahrungen und Vorstellungen auseinanderzusetzen.</p>
  </div>

  <div class="pill" style="left:403px;top:23px;width:144px;">Inhalte</div>
  <ul class="block bullets" style="left:422px;top:64px;">
    <li>- Einführung in die Bindungstheorie:<br>Eine sichere Basis für eine gute Entwicklung.</li>
    <li>- Die Bedürfnisse eines Kindes: Was braucht ein<br>Kind zu welcher Zeit? Auseinandersetzung mit<br>den wichtigsten Entwicklungsbereichen.</li>
    <li>- Was bedeutet Erziehung: Auseinandersetzung mit verschiedenen<br>Erziehungsmodellen und den eigenen Erfahrungen.</li>
    <li>- Elternschaft, Partnerschaft, Selbsterfüllung: Wie können<br>diese Bereiche gut miteinander vereinbart werden?</li>
    <li>- Vorstellung von Beratungs- und Hilfsangeboten: An welche Stelle<br>kann ich mich wenden, wenn ich Beratung oder Hilfe benötige?</li>
  </ul>

  <div class="pill" style="left:403px;top:267px;width:222px;">Weitere Informationen</div>
  <div class="block" style="left:422px;top:309px;">
    <p>Dieses Seminar sollte möglichst von beiden Elternteilen besucht<br>werden. Bei Interesse können auch andere Bezugspersonen des<br>Kindes teilnehmen. Z.B. die zukünftigen Großeltern, wenn sie<br>einen Teil der Betreuung des Kindes übernehmen sollen. Nach<br>dem Seminar wird es die Möglichkeit zum weiteren Austausch<br>zwischen den Eltern geben. Entweder im <span class="accent">velunora</span> Internetforum<br>oder in begleiteten Gruppentreffen.</p>
  </div>
  <div class="block small" style="left:422px;top:438px;">
    <p>Informationen zur Corona-Pandemie: Nach aktuellem Stand<br>können die Seminare unter 3G Bedingungen (geimpft, genesen<br>oder getestet) stattfinden.</p>
  </div>

  <h3 class="subhead" style="left:421px;top:499px;">Termine</h3>
  <div class="block dates" style="left:422px;top:520px;">
    <p>Seminar 1: 11.05. bis 22.06.2022, jeden MI 19-21 Uhr</p>
    <p>Seminar 2: 14.05. bis 15.05.2022, SA 10-18 Uhr, SO 10-16 Uhr</p>
    <p>Seminar 3: 25.06. bis 26.06.2022, SA 10-18 Uhr, SO 10-16 Uhr</p>
  </div>

  <h3 class="subhead" style="left:422px;top:592px;">Preis</h3>
  <div class="block" style="left:422px;top:612px;"><p>Pro Elternteil 175 € / Pro Elternpaar 300 €</p></div>
  <div class="block small" style="left:422px;top:633px;">
    <p>Sollte Ihnen die Finanzierung des Teilnahmepreises nicht<br>möglich sein, kann evtl. eine Unterstützung durch dritte Stellen<br>ermöglicht werden. Schreiben Sie dazu bitte eine Nachricht an<br>t.walduck@velunora.de.</p>
  </div>

  <h3 class="subhead" style="left:422px;top:710px;">Ort</h3>
  <div class="block" style="left:422px;top:730px;"><p>Jugendhaus Lindenhof, Amselweg 14, 32425 Mindenau</p></div>
</div>
</body>
</html>
```